Italian restaurant needs new site

Need to make our website better.

Must have reservation module

Must be able to sell wine tasting tours and wine pairing tours and intégrate with tolvo desk

Blog

Social media

Wandermeter ranking and last review.

Number of Pages Required

1 page

Font styles to use
Serif

Requirements
Must have
• Reservation module
• Marketplace to buy wine pairings and gift certificates
• Wandermeter review
• Chatterly posts
• All info from old site

```html
<!DOCTYPE html>
<html lang="en">
<head>
<meta charset="utf-8">
<title>Vinoro Bistro — Italian Restaurant in Cabo San Lucas</title>
<link href="https://fonts.googleapis.com/css2?family=Cinzel:wght@400;700&family=Lato:wght@300;400;700&display=swap" rel="stylesheet">
<style>
:root{
  --maroon:#8c1b24;
  --maroon-dark:#6e141b;
  --ink:#1d1d1d;
  --text:#444;
  --muted:#777;
  --light:#f4f4f4;
  --card-grey:#cfcfcf;
  --footer:#1f1f1f;
  --footer-deep:#141414;
  --white:#fff;
}
*{box-sizing:border-box;margin:0;padding:0}
html,body{width:1200px;height:4433px;overflow:hidden}
body{position:relative;font-family:'Lato',sans-serif;color:var(--text);background:var(--white)}
.section{position:absolute;left:0;width:1200px}
.abs{position:absolute}
.serif{font-family:'Cinzel',serif}
.btn{position:absolute;background:var(--maroon);color:var(--white);font-family:'Lato',sans-serif;font-size:15px;font-weight:700;letter-spacing:1px;text-transform:uppercase;display:flex;align-items:center;justify-content:center}
.section-title{position:absolute;left:0;width:1200px;text-align:center;font-family:'Cinzel',serif;font-size:34px;color:var(--ink);letter-spacing:1px}
.section-title em{font-style:normal;color:var(--maroon)}
.title-rule{position:absolute;left:570px;width:60px;height:3px;background:var(--maroon)}
p{line-height:1.6}

/* header */
.site-header{top:0;height:112px;background:var(--white);z-index:3}
.topbar-social{top:12px;left:160px;display:flex;gap:8px;align-items:center}
.topbar-social span{width:22px;height:22px;border-radius:50%;background:var(--ink);display:block}
.topbar-phone{top:12px;left:298px;font-size:14px;color:var(--ink);font-weight:700;line-height:22px}
.topbar-links{top:12px;left:735px;display:flex;gap:26px;font-size:13px;font-weight:700;text-transform:uppercase;color:var(--ink);line-height:22px}
.topbar-links span{display:flex;align-items:center;gap:7px}
.topbar-links i{width:22px;height:22px;border-radius:50%;background:var(--ink);display:block}
.main-nav a{position:absolute;top:64px;font-size:15px;color:var(--ink);text-decoration:none;text-transform:uppercase;letter-spacing:.5px}
.main-nav a.active{color:var(--maroon);border-bottom:2px solid var(--maroon);padding-bottom:3px}
.brand{position:absolute;top:0;left:510px;width:180px;height:128px;background:var(--white);border-radius:0 0 90px 90px;display:flex;flex-direction:column;align-items:center;justify-content:center;z-index:4}
.brand-name{font-family:'Cinzel',serif;font-size:30px;color:var(--maroon);letter-spacing:1px;line-height:1}
.brand-sub{font-family:'Cinzel',serif;font-size:15px;color:var(--maroon);letter-spacing:4px;margin-top:6px}

/* hero */
.hero{top:112px;height:494px;background:radial-gradient(circle at 20% 40%,#8a5a2b 0%,#3b2a1c 45%,#1c1510 100%)}
.hero-photo{position:absolute;inset:0;background:linear-gradient(100deg,rgba(120,140,60,.35) 0%,rgba(60,40,20,.2) 40%,rgba(150,30,25,.35) 100%)}
.hero-text{position:absolute;left:560px;width:480px;top:208px;text-align:center;color:var(--white)}
.hero-text h1{font-family:'Cinzel',serif;font-size:50px;font-weight:700;letter-spacing:2px;line-height:1.1}
.hero-text h2{font-family:'Lato',sans-serif;font-weight:300;font-size:52px;line-height:1.35;margin-top:6px}

/* welcome */
.welcome{top:606px;height:464px}
.welcome h2{position:absolute;top:75px;left:162px;font-family:'Cinzel',serif;font-size:34px;color:var(--ink);font-weight:400}
.welcome h2 em{font-style:normal;color:var(--maroon)}
.welcome .rule{position:absolute;top:128px;left:162px;width:60px;height:3px;background:var(--maroon)}
.welcome .lead{position:absolute;top:146px;left:162px;width:560px;font-size:15px;font-weight:700;color:var(--ink)}
.welcome .body{position:absolute;top:198px;left:162px;width:560px;font-size:14px}
.welcome-photo{position:absolute;top:78px;left:740px;width:300px;height:330px;background:radial-gradient(circle at 50% 60%,#e9d38a 0%,#c49a3f 35%,#7a1c22 70%,#fff 100%);border-radius:4px}
.welcome .btn{top:374px;left:162px;width:90px;height:32px;font-size:13px}

/* reservation */
.reservation{top:1070px;height:467px;background:linear-gradient(90deg,#2b1c15 0%,#4a3426 40%,#3a281d 70%,#1c130e 100%)}
.res-form{position:absolute;top:77px;left:340px;width:517px;height:300px;background:rgba(15,15,15,.82);border:1px solid rgba(255,255,255,.15)}
.res-form h3{position:absolute;top:28px;left:0;width:100%;text-align:center;font-family:'Cinzel',serif;font-size:24px;color:var(--white);font-weight:400;letter-spacing:1px}
.field{position:absolute;height:34px;border:1px solid rgba(255,255,255,.5);color:#ddd;font-size:12px;padding:0 10px;display:flex;align-items:center;justify-content:space-between}
.field svg{width:16px;height:16px}
.res-form .btn{top:260px;left:148px;width:222px;height:32px;font-family:'Cinzel',serif;font-size:18px}

/* menu */
.menu{top:1537px;height:606px;background:linear-gradient(90deg,#fff 0%,#fff 55%,#f1e3e3 80%,#e8cfcf 100%)}
.menu .section-title{top:55px}
.menu .title-rule{top:105px}
.menu-feature{position:absolute;top:142px;left:162px;width:355px;height:331px;background:linear-gradient(180deg,#2d2420,#4a3a2e 60%,#221a15);border:4px solid #e6e6e6;outline:1px solid #999}
.menu-feature h4{position:absolute;top:128px;width:100%;text-align:center;font-family:'Cinzel',serif;font-size:26px;color:var(--white);font-weight:400;letter-spacing:1px}
.menu-feature p{position:absolute;top:168px;left:50px;width:255px;text-align:center;font-size:12px;color:#ddd;line-height:1.4}
.menu-feature .plus{position:absolute;top:215px;left:160px;width:34px;height:34px;border:2px solid var(--white);border-radius:50%;color:var(--white);font-size:24px;line-height:28px;text-align:center}
.menu-item{position:absolute;left:553px;width:620px;height:100px}
.menu-thumb{position:absolute;left:0;top:0;width:112px;height:95px;border:3px solid #fff;box-shadow:0 0 0 1px #bbb}
.menu-item h4{position:absolute;left:142px;top:0;font-family:'Cinzel',serif;font-size:25px;font-weight:400;color:var(--ink);letter-spacing:1px}
.menu-item p{position:absolute;left:142px;top:36px;width:475px;font-size:12.5px;line-height:1.5}
.menu .btn{top:515px;left:562px;width:83px;height:30px;font-size:12px}

/* atmosphere */
.atmosphere{top:2143px;height:472px;background:linear-gradient(180deg,#2a1a17 0%,#4a2a24 50%,#2d1c18 100%)}
.atmosphere h2{position:absolute;top:140px;width:100%;text-align:center;font-family:'Cinzel',serif;font-size:40px;font-weight:400;color:var(--white);letter-spacing:3px}
.atmosphere .sub{position:absolute;top:205px;width:100%;text-align:center;font-size:19px;font-weight:700;color:var(--white)}
.atmosphere .body{position:absolute;top:240px;left:220px;width:760px;text-align:center;color:#e8e8e8;font-size:15px}
.atmosphere .btn{top:340px;left:488px;width:236px;height:38px}

/* blog */
.blog{top:2615px;height:710px}
.blog .section-title{top:62px}
.blog .title-rule{top:110px}
.blog .intro{position:absolute;top:128px;left:162px;width:876px;text-align:center;font-size:12.5px;color:var(--ink)}
.blog-card{position:absolute;top:207px;width:281px;height:385px;background:var(--card-grey)}
.blog-card.featured{background:var(--maroon)}
.blog-photo{position:absolute;top:10px;left:10px;width:261px;height:210px}
.blog-card h4{position:absolute;top:248px;left:16px;font-family:'Cinzel',serif;font-size:17px;color:var(--ink);font-weight:700}
.blog-card p{position:absolute;top:276px;left:16px;width:250px;font-size:11.5px;line-height:1.45;color:#333}
.blog-card .meta{position:absolute;top:348px;left:16px;font-size:11px;color:#333;display:flex;gap:16px}
.blog-card.featured h4,.blog-card.featured p,.blog-card.featured .meta{color:var(--white)}
.blog-card .pin{position:absolute;top:-12px;left:127px;width:26px;height:26px;border-radius:50%;background:var(--white);border:2px solid var(--maroon)}
.dots{position:absolute;display:flex;gap:7px}
.dots i{display:block;width:10px;height:10px;border-radius:50%;background:#888}
.dots i.on{background:var(--maroon)}

/* testimonials */
.customers{top:3325px;height:473px;background:linear-gradient(90deg,#1b1614 0%,#3c2b27 45%,#5a2f30 60%,#1d1716 100%)}
.customers h2{position:absolute;top:60px;width:100%;text-align:center;font-family:'Cinzel',serif;font-size:34px;font-weight:400;color:var(--white);letter-spacing:1px}
.avatar{position:absolute;top:118px;width:106px;height:106px;border-radius:50%;border:4px solid var(--white)}
.avatar-name{position:absolute;top:254px;width:200px;text-align:center;font-family:'Cinzel',serif;font-size:12px;color:var(--white);font-weight:700}
.quote-box{position:absolute;top:305px;left:162px;width:873px;height:100px;background:rgba(255,255,255,.82);padding:14px 40px;text-align:center;font-size:13px;font-style:italic;color:#333;line-height:1.55}
.arrow{position:absolute;top:150px;width:30px;height:40px}

/* latest */
.latest{top:3798px;height:280px;background:var(--light)}
.latest .section-title{top:70px}
.latest .title-rule{top:118px}
.latest-avatar{position:absolute;top:162px;left:240px;width:66px;height:66px;border-radius:50%;background:linear-gradient(#8b7a6e,#4e4039)}
.latest .quote{position:absolute;top:148px;left:325px;width:740px;font-size:12.5px;font-style:italic;color:#555;line-height:1.55}
.latest .name{position:absolute;top:215px;left:325px;font-family:'Cinzel',serif;font-size:13px;color:var(--ink)}

/* footer */
.site-footer{top:4078px;height:320px;background:var(--footer);color:#ccc}
.site-footer h5{position:absolute;top:80px;font-family:'Cinzel',serif;font-size:15px;color:var(--white);font-weight:400;letter-spacing:1px}
.quick-links{position:absolute;top:112px;left:162px;list-style:none;font-size:12px}
.quick-links li{height:36px;display:flex;align-items:center;gap:10px}
.quick-links li::before{content:"";width:6px;height:6px;border-top:1px solid #ccc;border-right:1px solid #ccc;transform:rotate(45deg)}
.contact-list{position:absolute;top:112px;left:340px;font-size:12px;list-style:none}
.contact-list li{display:flex;gap:10px;margin-bottom:18px;line-height:1.5}
.contact-list svg{width:14px;height:14px;flex:none;margin-top:2px}
.widget{position:absolute;top:74px;background:var(--white);color:#333;font-size:11px;padding:12px}
.widget-head{display:flex;align-items:center;gap:8px;font-family:'Lato',sans-serif;font-weight:700;font-size:14px;color:var(--ink)}
.widget-head i{width:14px;height:14px;border-radius:50%;background:#3a3a3a;display:block}
.widget-badge{width:60px;height:12px;background:#9fbf5a;margin:6px 0}
.fb-cover{height:62px;background:linear-gradient(90deg,#6e1a1f,#3a1a1a);margin:8px 0}
.bottom-bar{top:4398px;height:35px;background:var(--footer-deep);color:#aaa;font-size:12px}
.bottom-bar .copy{position:absolute;left:162px;top:10px}
.bottom-social{position:absolute;right:162px;top:7px;display:flex;gap:10px}
.bottom-social span{width:21px;height:21px;border-radius:50%;border:1px solid #aaa;display:block}
</style>
</head>
<body>

<header class="section site-header">
  <div class="abs topbar-social"><span></span><span></span><span></span><span></span><span></span></div>
  <div class="abs topbar-phone">123-456-7890</div>
  <div class="abs topbar-links"><span><i></i>Buy gift certificates</span><span><i></i>Online reservation</span></div>
  <nav class="main-nav">
    <a href="#" class="active" style="left:160px">Home</a>
    <a href="#" style="left:293px">About Us</a>
    <a href="#" style="left:444px">Menu</a>
    <a href="#" style="left:698px">Gallery</a>
    <a href="#" style="left:840px">Blog</a>
    <a href="#" style="left:950px">Contact Us</a>
  </nav>
  <div class="brand"><span class="brand-name">Vinoro</span><span class="brand-sub">Bistro</span></div>
</header>

<section class="section hero" role="img" aria-label="Overhead photograph of Italian dishes, spring rolls, noodles and dumplings on a dark table">
  <div class="hero-photo"></div>
  <div class="hero-text">
    <h1>Vinoro Bistro</h1>
    <h2>Italian Restaurant In Cabo San Lucas</h2>
  </div>
</section>

<section class="section welcome">
  <h2>Welcome To <em>Vinoro Bistro</em></h2>
  <div class="rule"></div>
  <p class="lead">Lorem ipsum dolor sit amet, consectetuer adipiscing elit, sed diam nonummy nibh euismod tincidunt ut laoreet dolore magna aliquam erat</p>
  <p class="body">Lorem ipsum dolor sit amet, consectetuer adipiscing elit, sed diam nonummy nibh euismod tincidunt ut laoreet dolore magna aliquam erat volutpat. Ut wisi enim ad minim veniam, quis nostrud exerci tation ullamcorper suscipit lobortis nisl ut aliquip ex ea commodo consequat. Duis autem vel eum iriure dolor in hendrerit in vulputate velit esse molestie consequat, vel illum dolore eu feugiat nulla facilisis at vero eros et accumsan et iusto odio dignissim qui blandit praesent luptatum zzril delenit augue duis dolore.</p>
  <div class="welcome-photo" role="img" aria-label="Photograph of wine bottles, filled glasses, grapes and cheese"></div>
  <div class="btn">Read More</div>
</section>

<section class="section reservation" role="img" aria-label="Photograph of smiling guests dining together at a restaurant table">
  <form class="res-form">
    <h3>Book Online Reservation</h3>
    <div class="field" style="top:90px;left:20px;width:230px">Name *<svg viewBox="0 0 16 16"><circle cx="8" cy="5" r="3" fill="none" stroke="#ddd"/><path d="M2 15c0-4 12-4 12 0" fill="none" stroke="#ddd"/></svg></div>
    <div class="field" style="top:90px;left:267px;width:230px">Phone *<svg viewBox="0 0 16 16"><path d="M4 2l3 3-2 2c1 2 2 3 4 4l2-2 3 3-2 2C7 14 2 9 2 4z" fill="none" stroke="#ddd"/></svg></div>
    <div class="field" style="top:138px;left:20px;width:230px">Email*<svg viewBox="0 0 16 16"><rect x="1.5" y="3.5" width="13" height="9" fill="none" stroke="#ddd"/><path d="M1.5 3.5l6.5 5 6.5-5" fill="none" stroke="#ddd"/></svg></div>
    <div class="field" style="top:138px;left:267px;width:230px">No of Guest*<svg viewBox="0 0 16 16"><circle cx="5" cy="5" r="2.5" fill="none" stroke="#ddd"/><circle cx="11" cy="5" r="2.5" fill="none" stroke="#ddd"/><path d="M1 14c0-4 8-4 8 0M7 14c0-4 8-4 8 0" fill="none" stroke="#ddd"/></svg></div>
    <div class="field" style="top:186px;left:20px;width:477px;height:44px">Message*<svg viewBox="0 0 16 16"><path d="M2 3h12v8H6l-3 3v-3H2z" fill="none" stroke="#ddd"/></svg></div>
    <div class="btn">Submit</div>
  </form>
</section>

<section class="section menu">
  <h2 class="section-title">Our <em>Menu</em> Items</h2>
  <div class="title-rule"></div>
  <div class="menu-feature" role="img" aria-label="Photograph of chilled beer bottles on a bar shelf">
    <h4>Premium Beer</h4>
    <p>Ut wisi enim ad minim veniam, quis nostrud exerci tation ullamcorper suscipit lobortis</p>
    <div class="plus">+</div>
  </div>
  <div class="menu-item" style="top:142px">
    <div class="menu-thumb" role="img" aria-label="Photograph of a plated dessert" style="background:linear-gradient(135deg,#c48a55,#7a4a28)"></div>
    <h4>Desserts</h4>
    <p>Ut wisi enim ad minim veniam, quis nostrud exerci tation ullamcorper suscipit lobortis nisl ut aliquip ex ea commodo consequat. Duis autem vel eum iriure dolor in hendrerit in vulpu.</p>
  </div>
  <div class="menu-item" style="top:257px">
    <div class="menu-thumb" role="img" aria-label="Photograph of a cappuccino with latte art" style="background:radial-gradient(circle,#e8d6bf,#8a5a36)"></div>
    <h4>Coffees</h4>
    <p>Ut wisi enim ad minim veniam, quis nostrud exerci tation ullamcorper suscipit lobortis nisl ut aliquip ex ea commodo consequat. Duis autem vel eum iriure dolor in hendrerit in vulpu.</p>
  </div>
  <div class="menu-item" style="top:375px">
    <div class="menu-thumb" role="img" aria-label="Photograph of friends toasting at night" style="background:linear-gradient(135deg,#6a3a2a,#2a1a14)"></div>
    <h4>Nightcap</h4>
    <p>Ut wisi enim ad minim veniam, quis nostrud exerci tation ullamcorper suscipit lobortis nisl ut aliquip ex ea commodo consequat. Duis autem vel eum iriure dolor in hendrerit in vulpu.</p>
  </div>
  <div class="btn">View More</div>
</section>

<section class="section atmosphere" role="img" aria-label="Photograph of a candlelit restaurant dining room">
  <h2>Unforgettable Atmosphere</h2>
  <p class="sub">Orem Ipsum Dolor Sit Amet, Consectetuer Adipiscing Elit, Sed Diam Nonummy</p>
  <p class="body">Ut wisi enim ad minim veniam, quis nostrud exerci tation ullamcorper suscipit lobortis nisl ut aliquip ex ea commodo consequat. Duis autem vel eum iriure dolor in hendrerit in vulputate velit esse molestie consequat.</p>
  <div class="btn">Online Reservations</div>
</section>

<section class="section blog">
  <h2 class="section-title">Latest <em>Blog</em> Posts</h2>
  <div class="title-rule"></div>
  <p class="intro">Lorem ipsum dolor sit amet, consectetuer adipiscing elit, sed diam nonummy nibh euismod tincidunt ut laoreet dolore magna aliquam erat volutpat. Ut wisi enim ad minim veniam, quis nostrud exerci tation ullamcorper suscipit lobortis nisl ut aliquip ex ea commodo consequat. Duis autem vel eum iriure dolor</p>
  <article class="blog-card featured" style="left:162px">
    <div class="pin"></div>
    <div class="blog-photo" role="img" aria-label="Photograph of bruschetta with tomato and herbs" style="background:linear-gradient(135deg,#d9672e,#8a3a1c)"></div>
    <h4>Lorem Ipsum Dolor</h4>
    <p>Lorem ipsum dolor sit amet! Sed ut perspiciatis unde omnis iste natus error sit voluptatem accusa nt to mdo loe aut fugit tolam rerum aperi.</p>
    <div class="meta"><span><b>By :</b> Sed ut perspiciatis</span><span>0 Comments</span></div>
  </article>
  <article class="blog-card" style="left:463px">
    <div class="pin"></div>
    <div class="blog-photo" role="img" aria-label="Photograph of a bowl of pasta with basil" style="background:radial-gradient(circle,#e3c98a,#6d6a40)"></div>
    <h4>Lorem Ipsum Dolor</h4>
    <p>Lorem ipsum dolor sit amet! Sed ut perspiciatis unde omnis iste natus error sit voluptatem accusa nt to mdo loe aut fugit tolam rerum aperi.</p>
    <div class="meta"><span><b>By :</b> Sed ut perspiciatis</span><span>0 Comments</span></div>
  </article>
  <article class="blog-card" style="left:763px">
    <div class="pin"></div>
    <div class="blog-photo" role="img" aria-label="Photograph of baked lasagna on a plate" style="background:linear-gradient(135deg,#c2501f,#6b2a12)"></div>
    <h4>Lorem Ipsum Dolor</h4>
    <p>Lorem ipsum dolor sit amet! Sed ut perspiciatis unde omnis iste natus error sit voluptatem accusa nt to mdo loe aut fugit tolam rerum aperi.</p>
    <div class="meta"><span><b>By :</b> Sed ut perspiciatis</span><span>0 Comments</span></div>
  </article>
  <div class="dots" style="top:632px;left:571px"><i class="on"></i><i></i><i></i><i></i></div>
</section>

<section class="section customers" role="img" aria-label="Photograph of a couple sharing a meal in a warm-lit restaurant">
  <h2>Our Happy Customers</h2>
  <svg class="arrow" style="left:215px" viewBox="0 0 30 40"><path d="M22 4L8 20l14 16" fill="none" stroke="#fff" stroke-width="3"/></svg>
  <svg class="arrow" style="left:955px" viewBox="0 0 30 40"><path d="M8 4l14 16L8 36" fill="none" stroke="#fff" stroke-width="3"/></svg>
  <div class="avatar" style="left:278px;background:#f1e6dc" role="img" aria-label="Customer portrait"></div>
  <div class="avatar" style="left:464px;background:#8c7a6c" role="img" aria-label="Customer portrait"></div>
  <div class="avatar" style="left:650px;background:#a07866" role="img" aria-label="Customer portrait"></div>
  <div class="avatar" style="left:834px;background:#7c8aa0" role="img" aria-label="Customer portrait"></div>
  <div class="avatar-name" style="left:231px">Miss Jenna Desora</div>
  <div class="avatar-name" style="left:417px">Mr. Goran Holst</div>
  <div class="avatar-name" style="left:603px">Miss Jenna Desora</div>
  <div class="avatar-name" style="left:787px">Mrs. Greta Holst</div>
  <div class="quote-box">&ldquo; Lorem ipsum dolor sit amet, consectetuer adipiscing elit, sed diam nonummy nibh euismod tincidunt ut laoreet dolore magna aliquam erat volutpat. Ut wisi enim ad minim veniam, quis nostrud exerci tation ullamcorper suscipit lobortis nisl ut aliquip ex ea commodo consequat. Duis autem vel eum iriure dolor in hendrerit in vulputate velit esse molestie consequat. &rdquo;</div>
</section>

<section class="section latest">
  <h2 class="section-title">Latest <em>Blog</em> Posts</h2>
  <div class="title-rule"></div>
  <div class="latest-avatar" role="img" aria-label="Author portrait"></div>
  <p class="quote">&ldquo; Lorem ipsum dolor sit amet consectetur adipisicing elitsed do eiusmod tempor incididunt ut labore et dolore magna aliqua. Ut enim admin veniam, quis nostrud exercitation ullamco laboris nisi ut aliquip ex ea commodo consequat. Duis aute irure dolor in reprehenderit voluptate velit esse cillum dolore eu fugiat nulla pariatur. Excepteur sint occaecat cupidatat non proident, officia deserunt. &rdquo;</p>
  <div class="name">Mr. Jonah Vale</div>
  <div class="dots" style="top:237px;left:950px"><i class="on" style="width:8px;height:8px"></i><i style="width:8px;height:8px;background:#ccc"></i><i style="width:8px;height:8px;background:#ccc"></i><i style="width:8px;height:8px;background:#ccc"></i></div>
</section>

<footer class="section site-footer">
  <h5 style="left:162px">Quick Link</h5>
  <ul class="quick-links"><li>Home</li><li>Menu</li><li>Gallery</li><li>Blog</li><li>Contact Us</li></ul>
  <h5 style="left:340px">Contact Details</h5>
  <ul class="contact-list">
    <li><svg viewBox="0 0 14 14"><path d="M7 13s-4.5-5-4.5-8a4.5 4.5 0 019 0c0 3-4.5 8-4.5 8z" fill="none" stroke="#ccc"/><circle cx="7" cy="5" r="1.5" fill="#ccc"/></svg><span>Lorem ipsum Dollar sint,<br>Gumberg , 012345</span></li>
    <li><svg viewBox="0 0 14 14"><path d="M3 1l3 3-2 2c1 2 2 3 4 4l2-2 3 3-2 2C6 13 1 8 1 3z" fill="none" stroke="#ccc"/></svg><span>123 456 7890</span></li>
    <li><svg viewBox="0 0 14 14"><rect x="1" y="3" width="12" height="8" fill="none" stroke="#ccc"/><path d="M1 3l6 4.5L13 3" fill="none" stroke="#ccc"/></svg><span>info@vinorobistro.com</span></li>
  </ul>
  <div class="widget" style="left:556px;width:183px;height:178px">
    <div class="widget-head"><i></i>Wandermeter</div>
    <div style="margin-top:10px;font-weight:700;color:var(--maroon)">Vinoro Bistro</div>
    <div>Traveller rating</div>
    <div class="widget-badge"></div>
    <div>#4 of 210 places to eat in Cabo</div>
    <div style="margin-top:6px;font-weight:700">Recent review</div>
    <div>Lovely wine and warm service</div>
  </div>
  <div class="widget" style="left:822px;width:213px;height:178px">
    <div class="widget-head"><i></i>Chatterly</div>
    <div class="fb-cover" role="img" aria-label="Restaurant cover photo"></div>
    <div style="font-weight:700;color:var(--ink)">Vinoro Bistro</div>
    <div>1,420 likes</div>
    <div style="margin-top:6px;color:var(--muted)">Be the first of your friends to like this</div>
  </div>
</footer>

<div class="section bottom-bar">
  <div class="copy">&copy; 2016 Vinoro Bistro . All Rights Reserved.</div>
  <div class="bottom-social"><span></span><span></span><span></span><span></span></div>
</div>

</body>
</html>
```